Dental office Stationary & Business card
Marlowe Pines Dental LLC
Dental office Stationary & Business card - Health
Creative Brief
Professional
Implants- Cosmetics- Generals- Braces
2815 Quarry Hollow Pkwy. Unit 3407 Norcross, GA 30071
mpdoffice@tinmail.example
www.marlowepinesdental.example
We would like designers to include for us the following: business card, letter head, envelope label, and e-signature template. logo design files can be downloaded below: https://www.filecrate.example/s/q8zrt3mw1xk5pa/Modern%20logo%20for%20a%20dental%20office.zip
Please have this content in the back of the card. "Your next appointment is on ____________ at _______ AM/PM

```html
<!DOCTYPE html>
<html lang="en">
<head>
<meta charset="utf-8">
<title>Marlowe Pines Dental — Business Card</title>
<link rel="stylesheet" href="https://fonts.googleapis.com/css2?family=Cormorant+Garamond:wght@600&family=Open+Sans:wght@400;600&display=swap">
<style>
  :root {
    --backdrop: #eceeef;
    --card: #ffffff;
    --brown: #6e3b22;
    --brown-dark: #5a2f1a;
    --tan: #b79c86;
    --taupe: #cfc2b6;
    --ink: #4a4a4a;
    --muted: #777777;
  }
  * { box-sizing: border-box; margin: 0; padding: 0; }
  html, body { width: 1200px; height: 939px; overflow: hidden; }
  body {
    background: var(--backdrop);
    font-family: "Open Sans", Arial, sans-serif;
    position: relative;
  }
  .card {
    position: absolute;
    width: 520px;
    height: 297px;
    background: var(--card);
    box-shadow: 0 6px 18px rgba(0,0,0,0.12);
    overflow: hidden;
  }
  .card--front { left: 60px; top: 321px; }
  .card--back { left: 620px; top: 321px; }

  .brand {
    display: flex;
    align-items: center;
    gap: 10px;
  }
  .brand__dot {
    width: 14px; height: 14px;
    border-radius: 50%;
    background: var(--brown);
    flex: none;
  }
  .brand__name {
    font-family: "Cormorant Garamond", Georgia, serif;
    font-weight: 600;
    color: var(--brown);
    letter-spacing: 1px;
    line-height: 1;
    white-space: nowrap;
  }
  .card--front .brand { position: absolute; left: 30px; top: 34px; }
  .card--front .brand__name { font-size: 24px; }

  .holder { position: absolute; left: 30px; top: 96px; }
  .holder__name { font-size: 16px; font-weight: 600; color: var(--ink); }
  .holder__title { font-size: 12px; color: var(--muted); margin-top: 2px; }

  .contact { position: absolute; left: 30px; top: 150px; list-style: none; }
  .contact li {
    display: flex; align-items: center; gap: 7px;
    font-size: 9.5px; color: var(--ink);
    line-height: 17px;
    white-space: nowrap;
  }
  .contact svg { width: 10px; height: 10px; flex: none; fill: var(--brown); }

  .swoosh { position: absolute; right: 0; bottom: 0; width: 300px; height: 297px; }

  .card--back .brand {
    position: absolute; left: 0; right: 0; top: 118px;
    justify-content: center;
  }
  .card--back .brand__name { font-size: 28px; }

  .appointment {
    position: absolute; left: 0; right: 0; top: 196px;
    text-align: center;
    font-size: 12px;
    color: var(--ink);
    white-space: nowrap;
  }
  .appointment__blank {
    display: inline-block;
    border-bottom: 1px solid var(--ink);
    vertical-align: baseline;
    height: 12px;
  }
  .appointment__blank--date { width: 120px; }
  .appointment__blank--time { width: 60px; }
</style>
</head>
<body>

<section class="card card--front">
  <div class="brand">
    <span class="brand__dot"></span>
    <span class="brand__name">MARLOWE PINES DENTAL</span>
  </div>

  <div class="holder">
    <p class="holder__name">Talia Brennholt</p>
    <p class="holder__title">Consultant</p>
  </div>

  <ul class="contact">
    <li><svg viewBox="0 0 10 10"><path d="M5 0a3.5 3.5 0 0 0-3.5 3.5C1.5 6 5 10 5 10s3.5-4 3.5-6.5A3.5 3.5 0 0 0 5 0zm0 5a1.5 1.5 0 1 1 0-3 1.5 1.5 0 0 1 0 3z"/></svg>2815 Quarry Hollow Pkwy. Unit 3407, Norcross, GA</li>
    <li><svg viewBox="0 0 10 10"><path d="M2 0l2 2.5-1.2 1.3a6 6 0 0 0 3.4 3.4L7.5 6 10 8l-1.5 2C4 10 0 6 0 1.5z"/></svg>T. 770 555 0148</li>
    <li><svg viewBox="0 0 10 10"><path d="M0 2h10v6H0zM0 2l5 3.5L10 2" stroke="#fff" stroke-width="0.8"/></svg>mpdoffice@tinmail.example</li>
    <li><svg viewBox="0 0 10 10"><circle cx="5" cy="5" r="5"/></svg>www.marlowepinesdental.example</li>
    <li><svg viewBox="0 0 10 10"><path d="M1 3h8v5H1zM3 0h4v3H3z"/></svg>F. 770 555 0149</li>
  </ul>

  <svg class="swoosh" viewBox="0 0 300 297" aria-hidden="true">
    <path d="M40 297 C 120 230, 220 170, 300 40 L 300 297 Z" fill="var(--taupe)"/>
    <path d="M80 297 C 150 245, 235 190, 300 80 L 300 297 Z" fill="var(--card)"/>
    <path d="M92 297 C 160 250, 240 200, 300 96 L 300 297 Z" fill="var(--tan)"/>
    <path d="M108 297 C 172 256, 246 210, 300 116 L 300 297 Z" fill="var(--brown)"/>
    <path d="M180 297 C 230 270, 275 235, 300 200 L 300 297 Z" fill="var(--brown-dark)" opacity="0.5"/>
  </svg>
</section>

<section class="card card--back">
  <div class="brand">
    <span class="brand__dot"></span>
    <span class="brand__name">MARLOWE PINES DENTAL</span>
  </div>
  <p class="appointment">Your next appointment is on <span class="appointment__blank appointment__blank--date"></span> at <span class="appointment__blank appointment__blank--time"></span> AM/PM</p>
</section>

</body>
</html>
```